Flyer-Design für Psychotherapeut
Schönes Design! Sehr gute und freundliche Kooperation! Gerne wieder!
Zielgruppe
Angeboten wird als Dienstleistung Psychotherapie, Coaching und Paarberatung
für Einzelpersonen (Männer/Frauen), Paare und Familien in schwierigen privaten und beruflichen Lebenssituationen.
Aufgabenstellung
Sehr geehrte Damen, sehr geehrte Herren,
gewünscht wird ein Falzflyer Hochformat, DIN-Lang, Wickelfalz, 6 bedruckte Seiten mit dem Endformat 10,0 x 21,0 cm. Ein entsprechendes Datenblatt der Druckerei finden Sie im Anhang.
Der Flyer wird auf einer Gesundheitsmesse eingesetzt und soll einen Überblick über mein Dienstleistungsangebot geben.
In der beigefügten Word Datei finden Sie einen von mir erstellten Flyer-Text-Entwurf. Er soll lediglich als Orientierung dienen. Weitere Infos erhalten Sie auf meiner Homepage
www.praxis-runkfeld-oswin.de.
Desweiteren erhalten Sie ein hochgeladenes Foto von mir, welches Sie bitte in Ihren Entwurf mit einbinden.
Ich bitte um Vorschläge für ein professionelles Design mit moderener gut lesbarer Schrift sowie farblich abgestimmten Blöcken des Inhalts.
Besonders wichtig ist mir die Orientierung an meinen Logofarben.
Das Logo wurde auch von entwurfhaus.de erstellt. Sie finden es unter meinen Projekten.
Für Rückfragen stehe ich Ihnen gerne zur Verfügung.
Freundliche Grüße
Sabine Runkfeld-Oswin

```html
<!DOCTYPE html>
<html lang="de">
<head>
<meta charset="utf-8">
<title>Falzflyer – Sabine Runkfeld-Oswin</title>
<link rel="stylesheet" href="https://fonts.googleapis.com/css2?family=Exo+2:ital,wght@0,600;0,700;1,700&family=Questrial&display=swap">
<style>
  :root{
    --orange:#e8610f;
    --orange-deep:#c9430b;
    --orange-light:#f39a3d;
    --peach:#fbd9bf;
    --grey-band:#d9d6d3;
    --text:#3b3b3b;
    --paper:#ffffff;
    --stage:#5a5d62;
  }
  *{box-sizing:border-box;margin:0;padding:0}
  html,body{width:1200px;height:1020px;overflow:hidden;background:var(--stage)}
  body{position:relative;font-family:"Questrial",sans-serif;color:var(--text)}

  .outside{position:absolute;top:180px;left:20px;width:448px;height:660px;display:flex;box-shadow:0 14px 30px rgba(0,0,0,.35)}
  .spread{position:absolute;top:180px;left:488px;width:672px;height:660px;display:flex;box-shadow:0 14px 30px rgba(0,0,0,.35)}
  .panel{position:relative;width:224px;height:660px;background:var(--paper);overflow:hidden;flex:none}
  .panel + .panel{border-left:1px solid #e4e1de}

  .top-band{position:absolute;left:0;top:0;width:100%;height:20px;background:linear-gradient(90deg,var(--orange-deep),var(--orange-light))}

  /* cover */
  .cover-head{position:absolute;top:0;left:0;width:100%;height:100px;background:linear-gradient(160deg,var(--orange-deep),var(--orange) 60%,var(--orange-light))}
  .brand{position:absolute;left:12px;top:32px;display:flex;align-items:center;gap:8px;color:#fff}
  .brand-dot{width:30px;height:30px;border-radius:50%;border:2px solid #fff;flex:none}
  .brand-name{font-size:14px;line-height:1;white-space:nowrap}
  .brand-tag{font-size:7px;margin-top:5px;white-space:nowrap}
  .cover-photo{position:absolute;top:100px;left:0;width:100%;height:370px;background:linear-gradient(180deg,#8e9a6e 0%,#a88a5c 35%,#7a5a36 75%,#5c4127 100%)}
  .cover-line{position:absolute;top:465px;left:0;width:100%}
  .badge{position:absolute;left:100px;top:400px;width:114px;height:114px;border-radius:50%;background:var(--orange);border:4px solid rgba(255,255,255,.85);display:flex;flex-direction:column;align-items:center;justify-content:center;color:#fff;font-family:"Exo 2",sans-serif;font-weight:600;font-size:13px;line-height:1.35;transform:rotate(-6deg)}
  .cover-claim{position:absolute;left:0;right:0;bottom:50px;text-align:center;color:var(--orange);font-size:16px;line-height:1.6}

  /* inner panels */
  .photo-area{position:absolute;top:20px;left:0;width:100%;height:140px;background:linear-gradient(120deg,#cfc6bc,#e9e3dc 55%,#b9b1a8)}
  .photo-couple{background:linear-gradient(120deg,#b9c3cf,#e6e8ea 55%,#a9a39b)}
  .grey-strip{position:absolute;top:20px;left:0;width:100%;height:30px;background:linear-gradient(180deg,var(--grey-band),#f1efed)}
  .panel-body{position:absolute;left:16px;right:14px}
  h2{font-family:"Exo 2",sans-serif;font-weight:700;font-style:italic;color:var(--orange-deep);font-size:14px;letter-spacing:.3px}
  h3{font-family:"Exo 2",sans-serif;font-weight:600;color:var(--orange);font-size:9px;line-height:1.3;margin-top:5px}
  p{font-size:7.5px;line-height:1.45;margin-top:7px}
  .ticks{list-style:none;margin-top:6px}
  .ticks li{position:relative;padding-left:14px;font-size:7.5px;line-height:1.35;margin-bottom:3px}
  .ticks li::before{content:"";position:absolute;left:2px;top:0;width:4px;height:7px;border-right:2px solid var(--orange);border-bottom:2px solid var(--orange);transform:rotate(40deg)}
  .services{background:linear-gradient(180deg,var(--peach) 0%,#fdeee2 45%,#fff 100%)}
  .section{margin-top:12px}
  .subline{font-family:"Exo 2",sans-serif;font-weight:600;color:var(--orange);font-size:7.5px;line-height:1.3;margin-top:3px}
  .subline-lg{font-size:9px}
</style>
</head>
<body>

<!-- Außenseite: Rückseite und Titel -->
<div class="outside">
  <section class="panel couples">
    <div class="top-band"></div>
    <div class="photo-area photo-couple" role="img" aria-label="Foto eines Paares im Gespräch"></div>
    <div class="panel-body" style="top:180px">
      <h2>PAARBERATUNG</h2>
      <div class="subline subline-lg">UNTERSTÜTZUNG IN KRISEN UND KONFLIKTEN</div>
      <ul class="ticks">
        <li>Wenn Sie nicht mehr miteinander reden können</li>
        <li>Wenn Missverständnisse und Konflikte zunehmen</li>
        <li>Wenn Sexualität und Nähe fehlen</li>
        <li>Wenn einer fremdgegangen ist</li>
        <li>Wenn Arbeitsbelastung die Beziehung belastet</li>
        <li>Wenn die Beziehung in Frage steht</li>
      </ul>
      <div class="section">
        <h2>TRENNUNGSBERATUNG/<br>MEDIATION</h2>
        <ul class="ticks">
          <li>Wenn Sie sich fair trennen möchten</li>
        </ul>
      </div>
    </div>
  </section>

  <section class="panel cover">
    <div class="cover-head">
      <div class="brand">
        <span class="brand-dot"></span>
        <div>
          <div class="brand-name">Sabine Runkfeld-Oswin</div>
          <div class="brand-tag">Psychotherapie&nbsp;|&nbsp;Coaching&nbsp;|&nbsp;Paarberatung</div>
        </div>
      </div>
    </div>
    <div class="cover-photo" role="img" aria-label="Foto einer Steintreppe, die durch Grün nach oben führt"></div>
    <svg class="cover-line" width="224" height="8" viewBox="0 0 224 8"><line x1="0" y1="7" x2="224" y2="1" stroke="#e8610f" stroke-width="2"/></svg>
    <div class="badge"><span>AUSWEGE</span><span>LÖSUNGSWEGE</span></div>
    <div class="cover-claim">Für mehr Zufriedenheit<br>im Privatleben und Beruf</div>
  </section>
</div>

<!-- Innenseiten -->
<div class="spread">
  <section class="panel about">
    <div class="top-band"></div>
    <div class="photo-area" role="img" aria-label="Porträtfoto der Therapeutin am Schreibtisch"></div>
    <div class="panel-body" style="top:180px">
      <h2>ÜBER MICH ...</h2>
      <p>Seit vielen Jahren begleite ich Menschen in Krisen und Umbrüchen. Mein Ziel ist es, gemeinsam mit Ihnen neue Wege zu finden und Ihre eigenen Kräfte zu stärken.</p>
    </div>
  </section>

  <section class="panel offer">
    <div class="top-band"></div>
    <div class="grey-strip"></div>
    <div class="panel-body" style="top:64px">
      <h2>MEIN ANGEBOT FÜR SIE</h2>
      <h3>BERATUNG- UND GESPRÄCHS&shy;THERAPIE NACH CARL RENDECK</h3>
      <h3>SYSTEMISCHES COACHING UND PAARBERATUNG</h3>
      <p>Als erfahrene Therapeutin, Beraterin und Coach begleite ich Sie als Einzelperson, Paar oder Familie in schwierigen Lebenssituationen und Neuorientierungsphasen.</p>
      <p>Ich unterstütze Sie einfühlsam und lösungsorientiert. Dabei nutze ich anerkannte, wirksame Therapie- und Beratungsmethoden, die ich gemeinsam mit Ihnen, auf Ihre persönlichen Bedürfnisse und Ziele abstimme.</p>
      <p>Im Mittelpunkt stehen Sie mit Ihrem Anliegen.</p>
      <p>Wir begegnen uns in einer Atmosphäre der Wertschätzung, Anteilnahme und absoluten Diskretion.</p>
      <h2 style="margin-top:16px">SIE KÖNNEN ...</h2>
      <ul class="ticks">
        <li>Bewältigungsstrategien entwickeln</li>
        <li>Ihre Fähigkeiten und Stärken entdecken</li>
        <li>Innere Blockaden überwinden</li>
        <li>Ihr Selbstvertrauen steigern</li>
        <li>Sich mutig und motiviert an Neues heranwagen</li>
        <li>Ihre Ziele umsetzen</li>
        <li>Ihr Leben und Ihre Partnerschaft so gestalten, wie Sie es sich wünschen.</li>
      </ul>
    </div>
  </section>

  <section class="panel services">
    <div class="top-band"></div>
    <div class="panel-body" style="top:38px">
      <h2>PSYCHOTHERAPIE</h2>
      <div class="subline">MEINE BEHANDLUNGSSCHWERPUNKTE:</div>
      <ul class="ticks">
        <li>Ängste- und Panikattacken</li>
        <li>Depression</li>
        <li>Erschöpfung/ Burnout</li>
        <li>Reaktion auf schwere Belastungen</li>
        <li>Psychosomatische Beschwerden</li>
        <li>Psychoonkologie</li>
        <li>Ostbrücker Gesundheitstraining</li>
      </ul>
      <div class="section">
        <h2>COACHING</h2>
        <div class="subline">BEGLEITUNG IN VERÄNDERUNGS&shy;PROZESSEN UND SCHWIERIGEN LEBENSPHASEN/-KRISEN</div>
        <ul class="ticks">
          <li>Veränderte Rahmenbedingungen im Privat- und Berufsleben wie z.B. Krankheit, Trennung, Trauer, Mobbing, Arbeitsplatzverlust u.a.</li>
          <li>Berufliche Neuorientierung</li>
          <li>Entscheidungsfindung</li>
          <li>Zielsetzung und Realisierung</li>
          <li>Lebensumbrüche wie z.B. Wechseljahre, Pensionierung u.a.</li>
        </ul>
      </div>
      <div class="section">
        <div class="subline subline-lg">PERSÖNLICHKEITSENTWICKLUNG</div>
        <ul class="ticks">
          <li>Konflikte erkennen und konstruktiv lösen</li>
          <li>Beziehungs- und Lebensgestaltung</li>
          <li>Eigene Stärken entdecken, weiter entwickeln und nutzen</li>
          <li>Stressbewältigung/ Burnoutprävention</li>
        </ul>
      </div>
    </div>
  </section>
</div>

</body>
</html>
```